Business card design needed

am looking for a fun and funky design to match our moto, seriously fun swimwear and fashion for girls.

We manufacture and retail girls swimwear and fashion in Australia. Our designs are fun loving and funky. I would like to use bright fuschia to match our website www.berrybloomwear.com.au. We target a higher end market so need it to reflect this.

Industry/Entity Type

Fashion

Contact Information for Business Card

Berry Bloom logo,
Melanie Drew
(07) 39514207
admin@berrybloomwear.com.au
www.berrybloomwear.com.au

Logo Text

Berry Bloom

```html
<!DOCTYPE html>
<html lang="en">
<head>
<meta charset="utf-8">
<title>Berry Bloom – Business Card</title>
<link rel="stylesheet" href="https://fonts.googleapis.com/css2?family=Questrial&family=Parisienne&display=swap">
<style>
  :root {
    --page-bg: #ecebee;
    --card-white: #ffffff;
    --violet-deep: #7a3cb0;
    --violet-mid: #a055b8;
    --orchid: #c878c4;
    --blush: #e6b3da;
    --fuchsia: #d62f8a;
    --faint-pink: #f4d3df;
    --ink-grey: #8a8a8a;
    --logo-white: #ffffff;
  }
  * { margin: 0; padding: 0; box-sizing: border-box; }
  html, body { width: 1200px; height: 1000px; overflow: hidden; }
  body {
    background: var(--page-bg);
    font-family: "Questrial", "Century Gothic", sans-serif;
    position: relative;
  }
  .card {
    position: absolute;
    left: 290px;
    width: 620px;
    height: 336px;
    overflow: hidden;
    box-shadow: 0 6px 22px rgba(60, 40, 70, 0.18);
  }
  .card--front { top: 120px; }
  .card--back { top: 540px; background: var(--card-white); }

  .front-backdrop {
    position: absolute; inset: 0;
    background:
      radial-gradient(ellipse at 78% 90%, rgba(240, 200, 232, 0.85) 0%, rgba(240, 200, 232, 0) 45%),
      radial-gradient(ellipse at 40% 75%, rgba(225, 160, 215, 0.7) 0%, rgba(225, 160, 215, 0) 50%),
      linear-gradient(155deg, var(--violet-deep) 0%, var(--violet-mid) 35%, var(--orchid) 70%, var(--blush) 100%);
  }
  .brand-lockup {
    position: absolute;
    left: 0; right: 0; top: 120px;
    text-align: center;
    color: var(--logo-white);
  }
  .brand-name {
    font-size: 62px;
    letter-spacing: 2px;
    line-height: 1;
  }
  .brand-tagline {
    margin-top: 10px;
    font-size: 11px;
    letter-spacing: 3.2px;
  }

  .back-watermark {
    position: absolute;
    left: 24px; top: 120px;
    font-size: 92px;
    color: var(--faint-pink);
    letter-spacing: 3px;
    white-space: nowrap;
    line-height: 1;
  }
  .contact-block {
    position: absolute;
    right: 50px; top: 195px;
    width: 260px;
  }
  .person-name {
    font-family: "Parisienne", cursive;
    font-size: 34px;
    color: var(--fuchsia);
    text-align: right;
    line-height: 1;
    margin-bottom: 12px;
  }
  .contact-line {
    display: flex;
    align-items: center;
    gap: 10px;
    font-size: 12.5px;
    color: var(--ink-grey);
    margin-bottom: 4px;
    padding-left: 22px;
  }
  .contact-line svg { flex: none; }
  .contact-line .accent { color: var(--fuchsia); }
</style>
</head>
<body>
  <section class="card card--front">
    <div class="front-backdrop" role="img" aria-label="Soft violet to pink gradient with glowing bokeh light spots"></div>
    <div class="brand-lockup">
      <div class="brand-name">Berry Bloom</div>
      <div class="brand-tagline">seriously fun swimwear and fashion for girls</div>
    </div>
  </section>

  <section class="card card--back">
    <div class="back-watermark" aria-hidden="true">Berry Bloom</div>
    <div class="contact-block">
      <div class="person-name">Melanie Drew</div>
      <div class="contact-line">
        <svg width="12" height="14" viewBox="0 0 12 14" aria-hidden="true">
          <rect x="2" y="0.5" width="8" height="13" rx="1.2" fill="var(--fuchsia)"/>
          <rect x="3.5" y="2" width="5" height="5" fill="#fff"/>
        </svg>
        <span>(07) 39514207</span>
      </div>
      <div class="contact-line">
        <svg width="14" height="10" viewBox="0 0 14 10" aria-hidden="true">
          <rect x="0" y="0" width="14" height="10" fill="var(--fuchsia)"/>
          <path d="M0 0 L7 6 L14 0" fill="none" stroke="#fff" stroke-width="1.2"/>
        </svg>
        <span>admin@<span class="accent">berrybloomwear</span>.com.au</span>
      </div>
      <div class="contact-line">
        <svg width="13" height="13" viewBox="0 0 14 14" aria-hidden="true">
          <circle cx="7" cy="7" r="6" fill="none" stroke="var(--fuchsia)" stroke-width="1.4"/>
          <ellipse cx="7" cy="7" rx="2.6" ry="6" fill="none" stroke="var(--fuchsia)" stroke-width="1.1"/>
          <line x1="1" y1="7" x2="13" y2="7" stroke="var(--fuchsia)" stroke-width="1.1"/>
        </svg>
        <span>www.<span class="accent">berrybloomwear</span>.com.au</span>
      </div>
    </div>
  </section>
</body>
</html>
```